Create Lanternfield HR Business Cards.

Create Business Cards for Lanternfield HR. 2 sided and Would like the back to have the logo.

Info for Business Card:
Address: 4827 Millbrook Ave Suite 230 Cleveland, Ohio 44987
Office Number: 216-555-0143
Mobile: 216-555-0192

Website: www.lanternfieldhr.example

Target Market(s)

Small to medium size businesses

Industry/Entity Type

Human Resources

Contact Information for Business Card

Company logo and information

Font styles to use
Serif
Sans Serif

Requirements
Must have
• Info for Business Card: Address: 4827 Millbrook Ave Suite 230 Cleveland, Ohio 44987 Office Number: 216-555-0143 Mobile: 216-555-0192 Website: www.lanternfieldhr.example

```html
<!DOCTYPE html>
<html lang="en">
<head>
<meta charset="utf-8">
<title>Lanternfield HR Business Cards</title>
<link href="https://fonts.googleapis.com/css2?family=Arimo:wght@400;700&display=swap" rel="stylesheet">
<style>
  :root {
    --navy: #27225f;
    --orange: #f48a24;
    --white: #ffffff;
    --backdrop: #eeeae6;
    --card-shadow: 0 6px 14px rgba(60, 40, 20, 0.22);
  }
  * { margin: 0; padding: 0; box-sizing: border-box; }
  html, body {
    width: 1200px;
    height: 1200px;
    overflow: hidden;
  }
  body {
    position: relative;
    background: var(--backdrop);
    font-family: "Arimo", Arial, sans-serif;
  }
  .card {
    position: absolute;
    left: 165px;
    width: 870px;
    height: 509px;
    background: var(--white);
    box-shadow: var(--card-shadow);
    overflow: hidden;
  }
  .card--front { top: 66px; }
  .card--back { top: 625px; }

  .front-swoosh {
    position: absolute;
    inset: 0;
    width: 100%;
    height: 100%;
  }

  .wordmark {
    position: absolute;
    display: flex;
    align-items: center;
    color: var(--navy);
    font-weight: 700;
    white-space: nowrap;
  }
  .wordmark__dot {
    flex: none;
    border-radius: 50%;
    background: var(--orange);
  }
  .card--front .wordmark {
    left: 72px;
    top: 150px;
    font-size: 31px;
    gap: 12px;
  }
  .card--front .wordmark__dot { width: 34px; height: 34px; }

  .card--back .wordmark {
    left: 50%;
    top: 50%;
    transform: translate(-50%, -50%);
    font-size: 54px;
    gap: 18px;
  }
  .card--back .wordmark__dot { width: 58px; height: 58px; }

  .contact-list {
    position: absolute;
    right: 62px;
    top: 330px;
    list-style: none;
    color: var(--white);
    font-size: 20px;
    font-weight: 400;
  }
  .contact-list__item {
    display: flex;
    justify-content: flex-end;
    align-items: center;
    height: 33.5px;
    gap: 20px;
  }
  .contact-list__icon {
    width: 16px;
    height: 16px;
    flex: none;
    fill: var(--white);
  }
</style>
</head>
<body>

  <section class="card card--front" aria-label="Business card front">
    <svg class="front-swoosh" viewBox="0 0 696 407" preserveAspectRatio="none" aria-hidden="true">
      <path fill="var(--navy)" d="M0,297 C210,335 520,270 600,0 L696,0 L696,407 L0,407 Z"/>
      <path fill="var(--orange)" d="M0,298 C240,332 540,262 614,0 L696,0 L696,407 L0,407 Z"/>
    </svg>

    <div class="wordmark">
      <span class="wordmark__dot"></span>
      <span class="wordmark__name">Lanternfield HR</span>
    </div>

    <ul class="contact-list">
      <li class="contact-list__item">
        <span>216-555-0143</span>
        <svg class="contact-list__icon" viewBox="0 0 24 24" aria-label="Office phone"><path d="M6.6 10.8a15.2 15.2 0 0 0 6.6 6.6l2.2-2.2a1 1 0 0 1 1-.25 11.4 11.4 0 0 0 3.6.57 1 1 0 0 1 1 1V20a1 1 0 0 1-1 1A17 17 0 0 1 3 4a1 1 0 0 1 1-1h3.5a1 1 0 0 1 1 1c0 1.25.2 2.45.57 3.57a1 1 0 0 1-.25 1z"/></svg>
      </li>
      <li class="contact-list__item">
        <span>216-555-0192</span>
        <svg class="contact-list__icon" viewBox="0 0 24 24" aria-label="Mobile"><path d="M7 1h10a2 2 0 0 1 2 2v18a2 2 0 0 1-2 2H7a2 2 0 0 1-2-2V3a2 2 0 0 1 2-2zm0 3v14h10V4zm5 15.5a1 1 0 1 0 0 2 1 1 0 0 0 0-2z"/></svg>
      </li>
      <li class="contact-list__item">
        <span>www.lanternfieldhr.example</span>
        <svg class="contact-list__icon" viewBox="0 0 24 24" aria-label="Website"><path d="M12 2a10 10 0 1 0 0 20 10 10 0 0 0 0-20zm6.9 6h-3a15.6 15.6 0 0 0-1.4-3.6A8 8 0 0 1 18.9 8zM12 4a14 14 0 0 1 1.9 4h-3.8A14 14 0 0 1 12 4zM4.3 14a8 8 0 0 1 0-4h3.4a16.5 16.5 0 0 0 0 4zm.8 2h3a15.6 15.6 0 0 0 1.4 3.6A8 8 0 0 1 5.1 16zm3-8h-3a8 8 0 0 1 4.4-3.6A15.6 15.6 0 0 0 8.1 8zM12 20a14 14 0 0 1-1.9-4h3.8A14 14 0 0 1 12 20zm2.3-6H9.7a14.7 14.7 0 0 1 0-4h4.6a14.7 14.7 0 0 1 0 4zm.2 5.6a15.6 15.6 0 0 0 1.4-3.6h3a8 8 0 0 1-4.4 3.6zm1.8-5.6a16.5 16.5 0 0 0 0-4h3.4a8 8 0 0 1 0 4z"/></svg>
      </li>
      <li class="contact-list__item">
        <span>4827 Millbrook Ave Suite 230 Cleveland, Ohio 44987</span>
        <svg class="contact-list__icon" viewBox="0 0 24 24" aria-label="Address"><path d="M12 2a7 7 0 0 0-7 7c0 5.2 7 13 7 13s7-7.8 7-13a7 7 0 0 0-7-7zm0 9.5a2.5 2.5 0 1 1 0-5 2.5 2.5 0 0 1 0 5z"/></svg>
      </li>
    </ul>
  </section>

  <section class="card card--back" aria-label="Business card back">
    <div class="wordmark">
      <span class="wordmark__dot"></span>
      <span class="wordmark__name">Lanternfield HR</span>
    </div>
  </section>

</body>
</html>
```